Business Card Design for Occupational Medicine Start Up Company

We need to design a professional business card. We are a healthcare company providing occupational medicine services to blue collar industries. We are professional, efficient and high quality service providers.

Target Market(s)

Blue Collar Industry: Shipbuilding, Ports, Trucking Companies; The Executives and Safety Officers for these companies

Industry/Entity Type

Healthcare

Contact Information for Business Card

Logo, Name, Title, Email, Phone

Other font styles liked:
• Please match our Brand Guide

Requirements
Must have
• Our Company Colors and Logo

```html
<!DOCTYPE html>
<html lang="en">
<head>
<meta charset="utf-8">
<title>CrewWell Clinics – Business Card</title>
<link href="https://fonts.googleapis.com/css2?family=Montserrat:wght@400;700;800&display=swap" rel="stylesheet">
<style>
  :root {
    --backdrop: #c9c9c9;
    --amber: #f7a83a;
    --cobalt: #0010cc;
    --white: #ffffff;
  }
  * { margin: 0; padding: 0; box-sizing: border-box; }
  html, body {
    width: 1200px;
    height: 846px;
    overflow: hidden;
    background: var(--backdrop);
    font-family: "Montserrat", Arial, sans-serif;
  }
  .card {
    position: absolute;
    left: 346px;
    width: 508px;
    height: 290px;
    border-radius: 36px;
  }
  .card--front { top: 114px; background: var(--amber); color: var(--cobalt); }
  .card--back  { top: 444px; background: var(--cobalt); color: var(--white); }

  /* Front: brand slot */
  .front-brand {
    position: absolute;
    left: 56px;
    top: 106px;
    display: flex;
    align-items: center;
    gap: 8px;
    font-weight: 800;
    font-size: 17px;
    letter-spacing: 0.02em;
  }
  .front-brand__dot {
    width: 22px; height: 22px;
    border-radius: 50%;
    background: var(--cobalt);
  }

  /* Front: person block */
  .person { position: absolute; left: 246px; top: 98px; }
  .person__name { font-weight: 800; font-size: 18px; line-height: 1; letter-spacing: 0.01em; }
  .person__title { font-weight: 700; font-size: 13px; margin-top: 4px; }

  .contact-list {
    position: absolute;
    left: 216px;
    top: 160px;
    list-style: none;
  }
  .contact-list__item {
    display: flex;
    align-items: center;
    height: 24px;
    font-size: 14px;
    font-weight: 400;
    letter-spacing: 0.01em;
  }
  .contact-list__icon {
    width: 20px; height: 20px;
    margin-right: 10px;
    fill: var(--cobalt);
    flex: none;
  }

  /* Back: brand lockup */
  .back-brand {
    position: absolute;
    left: 0; right: 0; top: 70px;
    display: flex;
    flex-direction: column;
    align-items: center;
    font-weight: 700;
  }
  .back-brand__dot {
    width: 76px; height: 76px;
    border-radius: 50%;
    background: var(--white);
    margin-bottom: 22px;
  }
  .back-brand__name { font-size: 33px; line-height: 1; letter-spacing: 0.01em; }
  .back-brand__sub { font-size: 17px; letter-spacing: 0.55em; margin-top: 8px; margin-right: -0.55em; }
</style>
</head>
<body>

<section class="card card--front">
  <div class="front-brand">
    <span class="front-brand__dot"></span>
    <span>CREWWELL</span>
  </div>

  <div class="person">
    <p class="person__name">FULL NAME</p>
    <p class="person__title">Title</p>
  </div>

  <ul class="contact-list">
    <li class="contact-list__item">
      <svg class="contact-list__icon" viewBox="0 0 24 24" aria-hidden="true"><path d="M6.6 2.5c.6-.3 1.3-.1 1.6.5l1.6 3.2c.3.6.1 1.2-.4 1.6l-1.3.9c.8 3.4 3 6.6 5.9 8.6l1.1-1.1c.5-.4 1.2-.5 1.7-.1l2.8 2.1c.5.4.6 1.1.3 1.7l-.8 1.2c-.7 1-2 1.4-3.1.9C10 19.6 5.3 13.6 4.6 6.4c-.1-1.2.6-2.3 1.6-2.9z"/></svg>
      <span>123-456-7890</span>
    </li>
    <li class="contact-list__item">
      <svg class="contact-list__icon" viewBox="0 0 24 24" aria-hidden="true"><path d="M2 5h20v14H2z M3.5 6.5 12 13l8.5-6.5" fill="var(--cobalt)" stroke="var(--amber)" stroke-width="1.2"/></svg>
      <span>full.name@crewwellclinics.com</span>
    </li>
    <li class="contact-list__item">
      <svg class="contact-list__icon" viewBox="0 0 24 24" aria-hidden="true"><circle cx="12" cy="12" r="10"/><path d="M2 12h20M12 2v20M4 7h16M4 17h16M12 2c-4 3-4 17 0 20M12 2c4 3 4 17 0 20" fill="none" stroke="var(--amber)" stroke-width="0.9"/></svg>
      <span>CREWWELLCLINICS.COM</span>
    </li>
  </ul>
</section>

<section class="card card--back">
  <div class="back-brand">
    <span class="back-brand__dot"></span>
    <span class="back-brand__name">CREWWELL</span>
    <span class="back-brand__sub">CLINICS</span>
  </div>
</section>

</body>
</html>
```